Business Card Design Project - ol taviran group

dear Sirs

we need business card design for our group ( OL Taviran Group ) , i have got the Logo design of our group from pixel forum in previous , so all need details relating to our group i think available with you, as well as the the chosen logo design

we hope to provide us with business card logo that to be appropaite and satisfactory to us .

thanks

note : logo design of our group is attached .

Reason: please extend the deadline of my project for additional 15 days because i didn't received appropriate design for our gruop yet . kindly beaware that i have received 77 design till now , supossed to send me 200-250 design at least . thanks

contents

name : Selim OR Haddani

position : Operation Manager

• person name

group logo
• logo color matching with back background

```html
<!DOCTYPE html>
<html lang="en">
<head>
<meta charset="utf-8">
<title>OL Taviran Group – Business Card</title>
<link rel="stylesheet" href="https://fonts.googleapis.com/css2?family=Arimo:wght@400;700&display=swap">
<style>
  :root {
    --stage: #000000;
    --paper: #ffffff;
    --brand-blue: #1d5aa3;
    --brand-blue-deep: #0d4a8c;
    --brand-blue-light: #1b70b8;
    --accent-rose: #c4958a;
    --accent-cream: #f6dcae;
    --accent-gold: #d9b46a;
  }
  html, body {
    margin: 0;
    padding: 0;
    width: 987px;
    height: 1200px;
    overflow: hidden;
    background: var(--stage);
    font-family: "Arimo", Arial, sans-serif;
  }
  .canvas { position: relative; width: 987px; height: 1200px; }

  .card {
    position: absolute;
    left: 113px;
    width: 772px;
    height: 472px;
    overflow: hidden;
  }
  .card--front { top: 119px; background: var(--paper); }
  .card--back {
    top: 647px;
    background: radial-gradient(circle at 45% 50%, var(--brand-blue-light) 0%, var(--brand-blue-deep) 75%);
  }

  .brand {
    position: absolute;
    display: flex;
    align-items: center;
    gap: 12px;
    font-weight: 700;
    font-size: 33px;
    letter-spacing: 1px;
    white-space: nowrap;
  }
  .brand__mark { width: 22px; height: 22px; background: var(--accent-gold); }
  .card--front .brand { left: 61px; top: 90px; color: var(--brand-blue); }
  .card--back .brand { left: 0; right: 0; top: 164px; justify-content: center; color: var(--paper); font-size: 44px; }

  .person { position: absolute; left: 76px; top: 232px; }
  .person__name { margin: 0; font-size: 24px; font-weight: 700; color: var(--accent-rose); line-height: 1.1; }
  .person__role { margin: 2px 0 0; font-size: 21px; color: var(--brand-blue); }

  .contact {
    position: absolute;
    left: 385px;
    top: 233px;
    margin: 0;
    padding: 0;
    list-style: none;
    font-size: 21px;
    line-height: 28px;
    color: var(--brand-blue);
  }
  .contact__label { color: var(--accent-rose); margin-right: 8px; }
  .contact__pobox { color: var(--accent-rose); }

  .side-strip {
    position: absolute;
    right: 0;
    top: 0;
    width: 55px;
    height: 100%;
    background: linear-gradient(180deg, var(--brand-blue-light), var(--brand-blue-deep));
  }
  .side-strip__url {
    position: absolute;
    left: 50%;
    top: 50%;
    transform: translate(-50%, -50%) rotate(-90deg);
    color: var(--paper);
    font-size: 25px;
    white-space: nowrap;
  }

  .back-url {
    position: absolute;
    left: 0;
    right: 0;
    top: 322px;
    text-align: center;
    font-size: 27px;
    font-weight: 700;
    color: var(--accent-cream);
  }

  .corner-decor { position: absolute; }
  .corner-decor--front {
    left: 0; bottom: 12px; width: 160px; height: 185px;
    background: linear-gradient(135deg, rgba(246,220,174,0.2), rgba(222,196,150,0.75));
    border-top-right-radius: 100% 100%;
  }
  .corner-decor--back {
    right: 0; bottom: 0; width: 142px; height: 205px;
    background: linear-gradient(135deg, rgba(160,170,190,0.15), rgba(150,160,180,0.6));
    border-top-left-radius: 100% 100%;
  }
</style>
</head>
<body>
<main class="canvas">
  <section class="card card--front">
    <div class="brand"><span class="brand__mark"></span>OL TAVIRAN GROUP</div>
    <div class="person">
      <p class="person__name">Selim OR Haddani</p>
      <p class="person__role">Operation Manager</p>
    </div>
    <ul class="contact">
      <li><span class="contact__label">t</span>+000 555 010 4821</li>
      <li><span class="contact__label">f</span>+000 555 020 6358</li>
      <li><span class="contact__label">m</span>+000 555 020 6358</li>
      <li><span class="contact__label">e</span>info@oltavirangroup.com</li>
      <li class="contact__pobox">po.box</li>
    </ul>
    <div class="corner-decor corner-decor--front" role="img" aria-label="Gold sweeping wing decoration"></div>
    <div class="side-strip"><span class="side-strip__url">www.oltavirangroup.com</span></div>
  </section>

  <section class="card card--back">
    <div class="brand"><span class="brand__mark"></span>OL TAVIRAN GROUP</div>
    <div class="back-url">www.oltavirangroup.com</div>
    <div class="corner-decor corner-decor--back" role="img" aria-label="Grey sweeping wing decoration"></div>
  </section>
</main>
</body>
</html>
```